Consulting Practice for Charities Needs A Brochure Deisgn

Hi! We need a tri-fold brochure for a Washington, DC based consulting practice that works with charities (NGOs, Associations, etc.) and wealthy donors (philanthropists). Our company, Morrow Civic Advisors, helps nonprofits to implement practices that maximize organizational efficiency and effectiveness - by working directly with board members and staff.
Our clients are well educated and quite sophisticated (some charities are international with multi-million dollar budgets, while others are quite local and small) This brochure will be handed to them by some of our 'referral partners' (law firms, accountants and even governmental agencies) in addition to being given out during our presentations. We draw inspiration from nature and would like to somehow include a "natural / eco-friendly" feel to the piece, including natural colors .... that being said, not in any way "folksy" - it must be sophisticated.

Target Market(s)

nonprofit executive directors, board chairs, wealth holders (philanthropists)

Industry/Entity Type

Consulting

Requirements
Must have
• I uploaded a word file with content (text) - most of that needs to be on the brochure ... but ... if it looks too crowded, let me know and I'll reduce
Nice to have
• pop-out quotes (maybe from testimonials??), nature - theme of some kind but also photo of boardroom (links to samples are like are uploaded in a word doc below)
Should not have
• nothing cute ... nothing too feminine

```html
<!DOCTYPE html>
<html lang="en">
<head>
<meta charset="utf-8">
<title>Morrow Civic Advisors – Brochure</title>
<link href="https://fonts.googleapis.com/css2?family=Lato:wght@300;400;700&display=swap" rel="stylesheet">
<style>
:root{
  --paper:#ffffff;
  --panel:#f7f7f5;
  --beige:#ebe9e0;
  --ink:#3d3d3d;
  --ink-soft:#4a4a4a;
  --heading:#1e8a3e;
  --green:#3bb14a;
  --lime:#8dc63f;
  --purple:#7b6fb6;
  --photo-a:#d9dde2;
  --photo-b:#8a8f96;
  --forest-a:#5d6e52;
  --forest-b:#2c3a2a;
}
*{box-sizing:border-box;margin:0;padding:0}
html,body{width:1200px;height:966px;overflow:hidden}
body{background:var(--paper);font-family:"Lato",sans-serif;color:var(--ink)}
.brochure{position:relative;width:1200px;height:966px;overflow:hidden}
.backdrop{position:absolute;inset:0}
.block{position:absolute}
.section-title{display:flex;align-items:center;gap:12px;font-weight:300;font-size:42px;color:var(--heading);line-height:1}
.section-icon{width:48px;height:48px;flex:none}
.intro{font-size:17px;line-height:22px;color:var(--ink-soft)}
.intro strong{font-weight:700}
.body-copy{font-size:14px;line-height:18.5px;color:var(--ink-soft)}
.sub-head{font-size:17px;font-weight:700;color:var(--ink);line-height:22px}
.sub-head.light{font-weight:400;color:#444}
ul.bullets{list-style:none}
ul.bullets li{position:relative;padding-left:12px;font-size:14px;line-height:18px;color:var(--ink-soft)}
ul.bullets li::before{content:"•";position:absolute;left:0;top:0}
.consultant-list li{margin-bottom:14px}
.service-list li{height:21.8px}
.result-title{font-size:19px;font-weight:700;text-align:center;color:var(--ink)}
.result{position:absolute;width:108px;height:108px;border-radius:50%;display:flex;align-items:center;justify-content:center;text-align:center;color:#fff;font-size:15px;line-height:18px}
.result.lime{background:var(--lime)}
.result.green{background:var(--green)}
.result.purple{background:var(--purple)}
</style>
</head>
<body>
<div class="brochure">
  <svg class="backdrop" width="1200" height="966" viewBox="0 0 1200 966">
    <defs>
      <linearGradient id="boardroomTone" x1="0" y1="0" x2="1" y2="1">
        <stop offset="0" stop-color="var(--photo-a)"/>
        <stop offset="1" stop-color="var(--photo-b)"/>
      </linearGradient>
      <linearGradient id="forestTone" x1="0" y1="0" x2="0" y2="1">
        <stop offset="0" stop-color="var(--forest-a)"/>
        <stop offset="1" stop-color="var(--forest-b)"/>
      </linearGradient>
    </defs>
    <rect x="404" y="0" width="396" height="480" fill="var(--panel)"/>
    <rect role="img" aria-label="Photo of a businesswoman presenting to colleagues around a boardroom table" x="800" y="0" width="400" height="480" fill="url(#boardroomTone)"/>
    <rect x="0" y="480" width="1200" height="486" fill="var(--beige)"/>
    <rect x="0" y="478" width="1200" height="3" fill="var(--green)"/>
    <rect role="img" aria-label="Photo of an evergreen forest along a calm lake with rocks" x="0" y="800" width="800" height="166" fill="url(#forestTone)"/>
  </svg>

  <div class="block" style="left:43px;top:56px">
    <div class="section-title">
      <svg class="section-icon" viewBox="0 0 48 48"><circle cx="24" cy="24" r="24" fill="var(--green)"/><circle cx="19" cy="18" r="5" fill="#fff"/><circle cx="29" cy="18" r="5" fill="#fff"/><path d="M10,33 C10,25 28,25 28,33 Z M22,33 C22,25 38,25 38,33 Z" fill="#fff"/></svg>
      <span>Who we are</span>
    </div>
  </div>
  <p class="block intro" style="left:49px;top:114px;width:710px"><strong>Founded in 2010 by Margaret Ellen Morrow,</strong> MCA was inspired by the national climate for stronger governance and deeper board engagement. Since then, we've worked with hundreds of board members to improve the impact of their philanthropic efforts.</p>
  <p class="block body-copy" style="left:49px;top:210px;width:335px">Our energetic and patient team of experts in nonprofit governance, operations and management will provide a comprehensive approach to problem solving, training and coaching.</p>
  <p class="block result-title" style="left:100px;top:306px;width:210px">The result?</p>
  <div class="result lime" style="left:37px;top:346px">Better<br>Boards</div>
  <div class="result green" style="left:152px;top:346px">Stronger<br>Organizations</div>
  <div class="result purple" style="left:271px;top:346px">Greater<br>Impact</div>

  <p class="block sub-head" style="left:436px;top:204px">MCA consultants will:</p>
  <ul class="block bullets consultant-list" style="left:436px;top:234px;width:330px">
    <li>Bring new perspectives and skills for strategic or generative (big picture) thinking</li>
    <li>Challenge your assumptions</li>
    <li>Offer innovative approaches to problem solving</li>
    <li>Identify sources of dysfunction</li>
    <li>Devise tactics to improve decision making or communication</li>
    <li>Make breakthrough improvements</li>
  </ul>

  <div class="block" style="left:43px;top:510px">
    <div class="section-title">
      <svg class="section-icon" viewBox="0 0 48 48"><circle cx="24" cy="24" r="24" fill="var(--green)"/><rect x="15" y="12" width="18" height="24" rx="2" fill="#fff"/><g stroke="var(--green)" stroke-width="2"><line x1="19" y1="19" x2="29" y2="19"/><line x1="19" y1="24" x2="29" y2="24"/><line x1="19" y1="29" x2="29" y2="29"/></g></svg>
      <span>What we do</span>
    </div>
  </div>
  <p class="block sub-head" style="left:49px;top:572px;color:#444">Organizational Clients</p>
  <div class="block body-copy" style="left:49px;top:594px;width:335px">
    <p>20th century developmental psychologist Henrik Aldane asserted that for individuals, conflict and crisis are positive and necessary; they are "sources of growth, strength, and commitment."</p>
    <p style="margin-top:18px">We believe the same can be true of organizations. MCA helps nonprofits manage change and emerge triumphantly. Through coaching, we help organizations implement practices to maximize efficiency and effectiveness - whether preparing</p>
  </div>
  <p class="block body-copy" style="left:440px;top:576px;width:310px">for transition, coping with chaos, or simply pursuing continued high performance - by working directly with board members and staff. Our methods are informed by research and honed by over 20 years of practice.</p>
  <p class="block sub-head" style="left:440px;top:694px;color:#444">Private Clients</p>
  <p class="block body-copy" style="left:440px;top:716px;width:290px">MCA philanthropic counsel helps individuals adopt impactful practices in their charitable endeavors.</p>

  <div class="block" style="left:851px;top:506px">
    <div class="section-title">
      <svg class="section-icon" viewBox="0 0 48 48"><circle cx="24" cy="24" r="24" fill="var(--green)"/><path d="M14,24 L21,31 L34,17" fill="none" stroke="#fff" stroke-width="5" stroke-linecap="round" stroke-linejoin="round"/></svg>
      <span>Our services</span>
    </div>
  </div>
  <p class="block sub-head light" style="left:858px;top:564px;width:320px;line-height:22px">Board and Senior Staff Coaching Workshops, Seminars and Retreats including:</p>
  <ul class="block bullets service-list" style="left:858px;top:636px;width:320px">
    <li>Roles &amp; Responsibilities</li>
    <li>Fundraising</li>
    <li>Succession Planning</li>
    <li>Board Self-Assessments</li>
    <li>Strategic Planning</li>
    <li>Board Recruitment Training</li>
    <li>Communications Development</li>
    <li>Grassroots Advocacy</li>
    <li>Mergers &amp; Acquisitions</li>
    <li>Philanthropic Counsel</li>
    <li>Board Placement</li>
    <li>Board Member Recruitment</li>
    <li>Board Retreat Planning &amp; Facilitation</li>
  </ul>
</div>
</body>
</html>
```